Website design for an events management company

What we need is the design of a website to be used by an events management company, the company is called "Velto Conference Services" and the website is expected to contain the following sections:
1) Homepage
2) Who are we?
3) Mission / Vision / Core values
4) Why to choose Velto?
5) Past experience
6) Duties or provided services (Scientific Program Duties, Accreditation, Fund Raising, Accommodations, Social Activities, Transportation, Marketing of the Event, Publications and printed materials, Secretarial Work and Media Coverage)
7) References
8) Contact Us page (will probably contain a contact us form plus email, address and a google map)

Attached for your reference the company's logo

Expected that the winner should deliver the designs of at least two pages (the homepage plus an inner page) plus of course all the used graphics, images ... etc.

Thanks

Target Market(s)

The design need to target scientific events and not public events, for example the company doesn't organize music concerts ... etc., it organizes only scientific events so please target business users (i.e. doctors, engineers, scientisits ... etc) while making the designs, including the correct colors, images and icons

Industry/Entity Type

It Company

Number of Pages Required

2 page

Requirements
Must have
• One homepage
• One inner page
• All the used graphics and images
Nice to have
• More than two pages

```html
<!DOCTYPE html>
<html lang="en">
<head>
<meta charset="utf-8">
<title>Velto Conference Services</title>
<link rel="stylesheet" href="https://fonts.googleapis.com/css2?family=Jost:wght@300;400&family=PT+Sans:wght@400;700&display=swap">
<style>
:root{
  --bar-dark:#252527;
  --header-bg:#e1e1e1;
  --logo-bg:#dcdcdc;
  --nav-active:#c6c6c6;
  --text-dark:#111;
  --tile-label:#555556;
  --tile-label-active:#000;
  --white:#fff;
  --caption-bg:rgba(232,236,246,.88);
}
*{margin:0;padding:0;box-sizing:border-box}
html,body{width:1200px;height:708px;overflow:hidden;background:var(--white)}
body{position:relative;font-family:"PT Sans",sans-serif;color:var(--text-dark)}
.top-bar{position:absolute;left:0;top:0;width:1200px;height:23px;background:var(--bar-dark)}
.site-header{position:absolute;left:0;top:23px;width:1200px;height:62px;background:var(--header-bg)}
.brand{position:absolute;left:153px;top:43px;width:155px;height:136px;background:var(--logo-bg);border-radius:0 0 5px 5px;z-index:3;display:flex;flex-direction:column;align-items:center;justify-content:center;gap:14px}
.brand-mark{display:flex;align-items:center;gap:8px;font-size:40px;font-weight:400;color:#6b6b6b;line-height:1}
.brand-dot{width:16px;height:16px;border-radius:50%;background:#6b6b6b}
.brand-name{font-size:13px;color:#555}
.main-nav{position:absolute;left:0;top:47px;width:1200px;height:36px;z-index:2}
.main-nav a{position:absolute;top:0;height:36px;line-height:36px;font-size:15px;color:var(--text-dark);text-decoration:none;letter-spacing:.2px}
.main-nav a.active{left:308px;width:107px;background:var(--nav-active);border-radius:4px 4px 0 0;text-align:center;font-size:20px;font-weight:700}
.hero{position:absolute;left:0;top:91px;width:1200px;height:505px;background:linear-gradient(100deg,#0d1a4a 0%,#23408e 25%,#5b86c6 45%,#9cc0e6 58%,#8fb6e0 75%,#a7c8ea 100%)}
.caption{position:absolute;left:149px;top:177px;width:539px;height:111px;background:var(--caption-bg);border-radius:5px;padding:14px 16px}
.caption h1{font-family:"Jost",sans-serif;font-weight:300;font-size:35px;line-height:1;letter-spacing:.5px;color:#000;white-space:nowrap}
.caption p{margin-top:6px;font-family:"Jost",sans-serif;font-size:11px;line-height:13px;text-align:justify;color:#111}
.slider-dots{position:absolute;left:610px;top:296px;display:flex;gap:3px}
.slider-dots span{width:13px;height:13px;border-radius:50%;background:rgba(225,232,244,.8)}
.slider-dots span.current{background:#fff}
.prev-btn{position:absolute;left:690px;top:441px;width:32px;height:32px;border-radius:50%;background:#e9eef5;display:flex;align-items:center;justify-content:center}
.services{position:absolute;left:727px;top:18px;display:grid;grid-template-columns:repeat(3,151px);grid-template-rows:repeat(3,150px);column-gap:3px;row-gap:3px}
.service-tile{display:flex;flex-direction:column;background:var(--white)}
.service-label{height:44px;background:var(--tile-label);color:#fff;font-size:12px;text-transform:uppercase;display:flex;align-items:center;justify-content:center;text-align:center;line-height:14px}
.service-tile.active .service-label{background:var(--tile-label-active)}
.service-photo{flex:1}
.site-footer{position:absolute;left:0;top:603px;width:1200px;height:89px;background:var(--header-bg);text-align:center;font-size:13px;line-height:19px;padding-top:22px}
.bottom-bar{position:absolute;left:0;top:692px;width:1200px;height:16px;background:var(--bar-dark)}
</style>
</head>
<body>
<div class="top-bar"></div>
<header class="site-header"></header>
<div class="brand">
  <div class="brand-mark"><span class="brand-dot"></span>Velto</div>
  <div class="brand-name">Velto Conference Services</div>
</div>
<nav class="main-nav">
  <a class="active" href="#">HOME</a>
  <a style="left:424px" href="#">WHO ARE WE?</a>
  <a style="left:553px" href="#">MISSION</a>
  <a style="left:634px" href="#">WHY TO CHOOSE VELTO?</a>
  <a style="left:812px" href="#">PAST EXPERIENCE</a>
  <a style="left:955px" href="#">REFERENCES</a>
  <a style="left:1065px" href="#">CONTACT</a>
</nav>
<section class="hero" role="img" aria-label="Upward view of a glass office tower against a blue sky">
  <div class="caption">
    <h1>SCIENTIFIC PROGRAM DUTIES</h1>
    <p>Lorem ipsum dolor sit amet, consectetur adipisci elit, sed eiusmod tempor incidunt ut labore et dolore magna aliqua. Ut enim ad minim veniam, quis nostrum exercitationem ullam corporis suscipit laboriosam, nisi ut aliquid ex ea commodi consequatur.</p>
  </div>
  <div class="slider-dots"><span class="current"></span><span></span><span></span><span></span><span></span></div>
  <div class="prev-btn"><svg width="12" height="18" viewBox="0 0 12 18"><path d="M9 1 L2 9 L9 17" fill="none" stroke="#222" stroke-width="1.8"/></svg></div>
  <div class="services">
    <div class="service-tile active"><div class="service-label">Scientific<br>Program Duties</div><div class="service-photo" role="img" aria-label="Speaker addressing a conference audience" style="background:linear-gradient(#9fb7d6,#24324c)"></div></div>
    <div class="service-tile"><div class="service-label">Accreditation</div><div class="service-photo" role="img" aria-label="Presenter in front of a seated audience" style="background:linear-gradient(#7a3a22,#2c2a3a)"></div></div>
    <div class="service-tile"><div class="service-label">Fund Raising</div><div class="service-photo" role="img" aria-label="Business people in a meeting" style="background:linear-gradient(#d8d4cf,#3b3f4a)"></div></div>
    <div class="service-tile"><div class="service-label">Accommodations</div><div class="service-photo" role="img" aria-label="Tablet showing a chart on a desk" style="background:linear-gradient(#c9b48f,#5a4a36)"></div></div>
    <div class="service-tile"><div class="service-label">Social Activities</div><div class="service-photo" role="img" aria-label="Scientist working in a laboratory" style="background:linear-gradient(#c9dced,#6f8fa8)"></div></div>
    <div class="service-tile"><div class="service-label">Transportation</div><div class="service-photo" role="img" aria-label="Passengers inside a car at dusk" style="background:linear-gradient(#5a2f4a,#2a1a2a)"></div></div>
    <div class="service-tile"><div class="service-label">Lorem Ipsum</div><div class="service-photo" role="img" aria-label="Computer keyboard and monitor on a desk" style="background:linear-gradient(#6c8aa6,#3a3a3a)"></div></div>
    <div class="service-tile"><div class="service-label">Lorem Ipsum</div><div class="service-photo" role="img" aria-label="Hand signing a document" style="background:linear-gradient(#5a5a5a,#eeeeee)"></div></div>
    <div class="service-tile"><div class="service-label">Lorem Ipsum</div><div class="service-photo" role="img" aria-label="Top view of a work table with laptop and papers" style="background:linear-gradient(#8c6a4a,#5a4330)"></div></div>
  </div>
</section>
<footer class="site-footer">
  <div>Home| Who are we?| Mission / Vision / Core values| Why to choose Velto?| Past experience| References| Contact</div>
  <div>©2015 Copyricht VELTO Conference Services. All Rights Reservede.</div>
</footer>
<div class="bottom-bar"></div>
</body>
</html>
```